Web Design for ROLV Air conditioning company

Hello,

I am calling on you for the modernization of the company's website
https://clarovent-services-techniques.fr/

The new one must include the new logo with the new graphic charter (color, style ...)

I'm looking for a simple design (less is more), a font written without Serif, the logo that brings a touch of color and modernity.

(maintenance and installation company for air conditioning and ventilation systems)
COLORS: in line with the logo

CHAPTER:

# PRESENTATION
# SERVICES
AIR CONDITIONING (ice cube icon)
HEATING (flame icon)
AIR TREATMENT (icon fan)
# ACHIEVEMENTS

# CONTACT
CONTACT FORM
GOOGLE MAPS

Target Market(s)

Showcase site for our customers

Coding

Coded - Design and coding required

Number of Pages Required

4 page

Font styles to use
Sans Serif

Colors
33b8a4
33a6d7
3176b5
ffffff

Requirements
Must have
• Clear and fluid navigation
a visual identity of the page with the logo
Should not have
• Overloaded.

```html
<!DOCTYPE html>
<html lang="en">
<head>
<meta charset="utf-8">
<title>ROLV – Air Conditioning, Heating &amp; Air Treatment</title>
<link href="https://fonts.googleapis.com/css2?family=Poppins:wght@500;600;700;800&family=Montserrat:wght@400;500;600&display=swap" rel="stylesheet">
<style>
:root{
  --teal:#33b8a4;
  --green:#3cc58e;
  --sky:#33a6d7;
  --blue:#3176b5;
  --white:#ffffff;
  --ink:#1d2b6b;
  --text:#555d66;
  --dark:#27313a;
  --darker:#1f2830;
  --head:"Poppins",sans-serif;
  --body:"Montserrat",sans-serif;
}
*{margin:0;padding:0;box-sizing:border-box}
html,body{width:1200px;height:4525px;overflow:hidden}
body{position:relative;background:var(--white);font-family:var(--body);color:var(--text)}
.abs{position:absolute}
.logo{font-family:var(--head);font-weight:800;color:var(--teal);letter-spacing:2px}

/* header */
.site-header .logo{left:93px;top:14px;font-size:40px}
.nav{top:34px;left:455px;display:flex;gap:54px;font-family:var(--head);font-weight:600;font-size:13px;color:#2b2f3a}
.btn-appoint{left:929px;top:22px;width:176px;height:40px;border-radius:20px;background:linear-gradient(90deg,var(--teal),var(--blue));color:#fff;font-family:var(--head);font-weight:600;font-size:12.5px;display:flex;align-items:center;justify-content:center}

/* hero */
.hero-photo{left:430px;top:0;width:770px;height:700px;background:linear-gradient(160deg,#f4f4f4,#dcdfe3 60%,#eef0f2)}
.hero-shape{left:0;top:0}
.hero-kicker{left:93px;top:252px;color:#fff;font-family:var(--head);font-weight:500;font-size:19px}
.hero-title{left:93px;top:282px;color:#fff;font-family:var(--head);font-weight:800;font-size:64px;line-height:76px}
.hero-sub{left:93px;top:441px;color:#fff;font-weight:600;font-size:13px}
.btn-light{left:93px;top:475px;width:177px;height:52px;border-radius:26px;background:#fff;color:var(--ink);font-family:var(--head);font-weight:600;font-size:15px;display:flex;align-items:center;justify-content:center}
.hero-arrows{left:93px;top:583px;display:flex;gap:10px}
.hero-arrows span{width:33px;height:33px;border-radius:50%;border:1.5px solid rgba(255,255,255,.8);display:flex;align-items:center;justify-content:center}
.hero-arrows span.on{background:#fff}

/* about */
.kicker{font-family:var(--head);font-weight:600;font-size:14px;color:var(--sky);letter-spacing:.5px}
.h2{font-family:var(--head);font-weight:800;color:var(--ink)}
.para{font-size:15px;line-height:26px;color:var(--text)}
.about-kicker{left:165px;top:775px}
.about-title{left:165px;top:792px;font-size:46px;line-height:56px}
.about-text{left:165px;top:915px;width:455px}
.about-room{left:712px;top:724px;width:393px;height:409px;border-radius:18px;background:linear-gradient(150deg,#c9cfdc,#8d9ec2 55%,#6f83b0)}
.about-tech{left:608px;top:1032px;width:204px;height:214px;border-radius:12px;background:linear-gradient(180deg,#cfd4da,#3b4d7d)}

/* services */
.services{left:0;top:1268px;width:1200px;height:588px;background:linear-gradient(90deg,var(--teal),var(--sky) 55%,var(--blue));overflow:hidden}
.ghost{position:absolute;font-family:var(--head);font-weight:800;color:rgba(255,255,255,.16);font-size:128px;letter-spacing:4px;writing-mode:vertical-rl;transform:rotate(180deg);line-height:1}
.svc-kicker{left:0;width:1200px;top:42px;text-align:center;color:#fff;font-family:var(--head);font-weight:600;font-size:13px}
.svc-title{left:0;width:1200px;top:54px;text-align:center;color:#fff;font-family:var(--head);font-weight:800;font-size:54px}
.svc-photo{left:462px;top:142px;width:276px;height:276px;border-radius:50%;background:radial-gradient(circle at 45% 35%,#e8f1f8,#9fc3df 70%,#84b2d6)}
.svc-item{color:#fff;width:220px}
.svc-item h3{font-family:var(--head);font-weight:600;font-size:15px;margin-bottom:6px}
.svc-item p{font-size:14px;line-height:21px}

/* achievements */
.ach-tri{left:0;top:1855px}
.ach-photo{left:660px;top:1925px;width:440px;height:700px;background:linear-gradient(180deg,rgba(236,238,241,.9),rgba(226,229,233,.85) 70%,rgba(232,170,70,.55))}
.ach-kicker{left:93px;top:2098px}
.ach-title{left:93px;top:2108px;font-size:54px}
.ach-text{left:93px;top:2190px;width:450px}
.badges{left:93px;top:2312px;display:flex;gap:76px}
.badges span{width:40px;height:40px;border-radius:50%;background:linear-gradient(135deg,var(--teal),var(--green))}
.badges span:nth-child(2){border-radius:8px}
.badges span:nth-child(3){background:linear-gradient(135deg,var(--sky),var(--teal))}
.badges span:nth-child(4){background:linear-gradient(135deg,#f2a23a,#e04b3a)}

/* testimonials */
.testi{left:142px;top:2686px;width:916px;height:579px;background:linear-gradient(120deg,#3dbb9c,var(--teal) 35%,var(--sky) 80%,#3a90c8);box-shadow:0 12px 30px rgba(0,0,0,.12);color:#fff;text-align:center;overflow:hidden}
.testi .t-k{position:absolute;top:80px;width:100%;font-family:var(--head);font-weight:600;font-size:13px}
.testi .t-h{position:absolute;top:98px;width:100%;font-family:var(--head);font-weight:800;font-size:54px}
.testi .quote{position:absolute;top:182px;left:0;width:100%;font-family:var(--head);font-weight:800;font-size:130px;line-height:1}
.testi .t-p{position:absolute;top:268px;left:110px;width:696px;font-size:16.5px;line-height:30px}
.testi .t-n{position:absolute;top:384px;width:100%;font-family:var(--head);font-weight:500;font-size:22px}
.dots{position:absolute;top:480px;left:425px;display:flex;gap:16px}
.dots i{width:10px;height:10px;border-radius:50%;background:rgba(255,255,255,.45)}
.dots i:first-child{background:#fff}

/* contact */
.contact{left:0;top:3353px;width:600px;height:650px;background:linear-gradient(180deg,var(--blue),#3a7fc0 50%,#3a88c7)}
.contact h2{position:absolute;top:80px;width:100%;text-align:center;color:#fff;font-family:var(--head);font-weight:600;font-size:38px}
.field{position:absolute;left:122px;width:450px;height:62px;border:1.5px solid rgba(255,255,255,.8);border-radius:31px;color:#fff;font-size:15px;padding:20px 28px}
.field.msg{height:152px;border-radius:24px}
.btn-send{position:absolute;left:122px;top:543px;width:450px;height:62px;border-radius:31px;background:linear-gradient(90deg,var(--green),var(--teal) 50%,var(--sky));color:#fff;font-family:var(--head);font-weight:600;font-size:15px;display:flex;align-items:center;justify-content:center;gap:10px}
.map{left:600px;top:3353px;width:600px;height:650px;background:linear-gradient(135deg,#eef0ec,#e4e7e3 50%,#eceee9)}

/* newsletter */
.news{left:0;top:4003px;width:1200px;height:162px;background:var(--dark)}
.news .n-k{position:absolute;left:95px;top:50px;color:var(--teal);font-size:15px}
.news .n-h{position:absolute;left:93px;top:62px;color:#fff;font-family:var(--head);font-weight:700;font-size:40px}
.news .n-in{position:absolute;left:326px;top:59px;width:324px;height:54px;border-radius:27px;background:#fff;color:#8a9098;font-size:12.5px;display:flex;align-items:center;padding-left:20px;gap:10px}
.news .n-btn{position:absolute;left:656px;top:59px;width:138px;height:54px;border-radius:27px;background:linear-gradient(90deg,var(--teal),var(--sky));color:#fff;font-family:var(--head);font-weight:600;font-size:14px;display:flex;align-items:center;justify-content:center}
.news .follow{position:absolute;left:838px;top:76px;color:#fff;font-family:var(--head);font-weight:600;font-size:15px}
.social{position:absolute;top:62px;width:48px;height:48px;border-radius:50%}

/* footer */
.footer{left:0;top:4165px;width:1200px;height:360px;background:var(--darker);color:#c9ced4}
.footer .logo{position:absolute;left:93px;top:68px;font-size:46px}
.footer .f-about{position:absolute;left:93px;top:155px;width:200px;font-size:12.5px;line-height:21px}
.f-col{position:absolute;top:72px;font-size:12.5px;line-height:20px}
.f-col h4{color:#fff;font-family:var(--head);font-weight:600;font-size:13px;margin-bottom:18px}
.f-col li{list-style:none;margin-bottom:13px;padding-left:13px;position:relative}
.f-col li::before{content:"";position:absolute;left:0;top:8px;width:5px;height:5px;border-radius:50%;background:var(--teal)}
.f-row{display:flex;gap:8px}
.copy{position:absolute;top:320px;width:100%;text-align:center;font-size:12.5px;color:#aab0b7}
.copy b{color:var(--teal);font-weight:600}
.footer .line{position:absolute;left:93px;top:300px;width:1012px;height:1px;background:rgba(255,255,255,.08)}
.top-btn{position:absolute;left:1068px;top:306px;width:38px;height:38px;border-radius:50%;background:var(--teal);display:flex;align-items:center;justify-content:center}
</style>
</head>
<body>

<!-- hero -->
<div class="abs hero-photo" role="img" aria-label="Technician servicing a wall-mounted air conditioning unit"></div>
<svg class="abs hero-shape" width="470" height="860" viewBox="0 0 470 860">
  <defs><linearGradient id="heroG" x1="0" y1="0" x2="0.6" y2="1">
    <stop offset="0" stop-color="#2d9bb8"/><stop offset="0.55" stop-color="#35b7a0"/><stop offset="1" stop-color="#3ec58c"/></linearGradient></defs>
  <path d="M0 0 H390 C440 110 470 300 440 400 C430 430 420 440 400 460 L0 855 Z" fill="url(#heroG)"/>
</svg>

<header class="site-header">
  <div class="abs logo">ROLV</div>
  <nav class="abs nav"><span>Presentation</span><span>Services &#8964;</span><span>Achievements</span><span>Contact</span></nav>
  <div class="abs btn-appoint">Make an Appointment</div>
</header>

<div class="abs hero-kicker">Clarovent Services</div>
<h1 class="abs hero-title">Industry<br>Grenoble</h1>
<div class="abs hero-sub">The solution to your maintenance problem</div>
<div class="abs btn-light">More Info</div>
<div class="abs hero-arrows">
  <span><svg width="10" height="12" viewBox="0 0 10 12"><path d="M7 1 L2 6 L7 11" stroke="#fff" stroke-width="1.6" fill="none"/></svg></span>
  <span class="on"><svg width="10" height="12" viewBox="0 0 10 12"><path d="M3 1 L8 6 L3 11" stroke="#2f9fb5" stroke-width="1.6" fill="none"/></svg></span>
</div>

<!-- about -->
<section>
  <div class="abs kicker about-kicker">WHO WE ARE</div>
  <h2 class="abs h2 about-title">Clarovent Services<br>Techniques</h2>
  <p class="abs para about-text">Lorem ipsum dolor sit amet, consr adipicing elit. Sed tristique impiet eros, suscit plaat turpis blandit eleetum. Suspendisse aliquam aliquet nisl. Ut a magna diam. Curabitur dolor neque, eleifd in plaerat in, mattis ut elit. Proin tincidunt, dui a mollis maximus, est dui aliquet risus,</p>
  <div class="abs about-room" role="img" aria-label="Bright blue room with an air conditioner above a lounge chair"></div>
  <div class="abs about-tech" role="img" aria-label="Technician installing an indoor air conditioning unit"></div>
</section>

<!-- services -->
<section class="abs services">
  <div class="ghost" style="left:38px;top:290px">OUR</div>
  <div class="ghost" style="left:1060px;top:0">SERVICE</div>
  <div class="abs svc-kicker">OUR SERVICES</div>
  <h2 class="abs svc-title">What We Do</h2>
  <div class="abs svc-photo" role="img" aria-label="Hand holding a remote control under an air conditioner"></div>
  <svg class="abs" style="left:380px;top:250px" width="440" height="260" viewBox="0 0 440 260">
    <path d="M31 32 A190 190 0 0 0 409 32" fill="none" stroke="#fff" stroke-width="1.5"/>
    <g>
      <circle cx="31" cy="32" r="26" fill="#fff" stroke="#3a8fc6" stroke-width="2"/>
      <rect x="22" y="25" width="18" height="15" rx="2" fill="none" stroke="#3a8fc6" stroke-width="1.6"/>
      <line x1="31" y1="25" x2="31" y2="40" stroke="#3a8fc6" stroke-width="1.4"/><line x1="22" y1="32" x2="40" y2="32" stroke="#3a8fc6" stroke-width="1.4"/>
    </g>
    <g>
      <circle cx="405" cy="32" r="26" fill="#fff" stroke="#3a8fc6" stroke-width="2"/>
      <path d="M405 20 C398 28 396 34 399 40 C402 45 408 45 411 40 C414 34 410 30 408 26 C407 31 405 32 403 31 C405 27 406 24 405 20 Z" fill="none" stroke="#3a8fc6" stroke-width="1.6"/>
    </g>
    <g>
      <circle cx="221" cy="217" r="26" fill="#fff" stroke="#3a8fc6" stroke-width="2"/>
      <circle cx="221" cy="217" r="2.5" fill="#3a8fc6"/>
      <path d="M221 214 C216 206 222 202 226 205 C228 208 225 212 221 214 M224 218 C232 214 236 220 233 224 C230 226 226 223 224 218 M218 219 C214 227 208 224 208 220 C209 216 214 216 218 219" fill="none" stroke="#3a8fc6" stroke-width="1.5"/>
    </g>
  </svg>
  <div class="abs svc-item" style="left:150px;top:265px;text-align:right"><h3>Air Conditioning</h3><p>Lorem ipsum dolor sit amet, consectetur adipiscing elit.</p></div>
  <div class="abs svc-item" style="left:828px;top:265px"><h3>Heating</h3><p>Lorem ipsum dolor sit amet, consectetur adipiscing elit.</p></div>
  <div class="abs svc-item" style="left:490px;top:508px;text-align:center"><h3>Air Treatment</h3><p>Lorem ipsum dolor sit amet, consectetur adipiscing elit.</p></div>
</section>

<!-- achievements -->
<section>
  <svg class="abs ach-tri" width="1200" height="910" viewBox="0 0 1200 910">
    <defs><linearGradient id="triG" x1="0" y1="0" x2="0" y2="1">
      <stop offset="0" stop-color="#2c9bb0"/><stop offset="1" stop-color="#3ec58c"/></linearGradient></defs>
    <path d="M1200 70 L1200 900 L880 760 Z" fill="url(#triG)"/>
  </svg>
  <div class="ghost" style="left:12px;top:2370px;color:rgba(60,70,80,.13);font-size:110px">OUR</div>
  <div class="ghost" style="left:680px;top:1860px;color:rgba(60,70,80,.13);font-size:110px;height:800px;overflow:hidden">ACHIEVEMEN</div>
  <div class="abs ach-photo" role="img" aria-label="Smiling worker in white t-shirt and yellow gloves giving a thumbs up"></div>
  <div class="abs kicker ach-kicker">ACHIEVEMENTS</div>
  <h2 class="abs h2 ach-title">Our Achivements</h2>
  <p class="abs para ach-text">Lorem ipsum dolor sit amet, consr adipicing elit. Sed tristique impiet eros, suscit plaat turpis blandit eleetum. Sed tristique impiet eros, suscit plaat turpis blandit eleetum.</p>
  <div class="abs badges"><span></span><span></span><span></span><span></span><span></span></div>
</section>

<!-- testimonials -->
<section class="abs testi">
  <svg style="position:absolute;left:0;top:0" width="916" height="579" viewBox="0 0 916 579">
    <path d="M0 0 H340 C300 60 260 120 120 150 C60 165 20 200 0 240 Z" fill="rgba(255,255,255,.07)"/>
    <path d="M0 579 V470 C140 420 300 520 520 480 C700 450 820 400 916 420 V579 Z" fill="rgba(255,255,255,.07)"/>
  </svg>
  <div class="t-k">TESTIMONIALS</div>
  <h2 class="t-h">What our clients say</h2>
  <div class="quote">&ldquo;</div>
  <p class="t-p">Etiam facilisis purus non mi accumn pharetra eu mattis lorem. Class apent taciti sociosqu ad litora torquent per conubia nostra, per inceptos himenaeos. Cras sed diam nec sapien luctus accumsan.</p>
  <div class="t-n">Lorem ipsum</div>
  <div class="dots"><i></i><i></i><i></i></div>
</section>

<!-- contact -->
<section class="abs contact">
  <h2>Get In Touch</h2>
  <div class="field" style="top:153px">Name</div>
  <div class="field" style="top:223px">Email</div>
  <div class="field" style="top:293px">Phone</div>
  <div class="field msg" style="top:377px">Message</div>
  <div class="btn-send"><svg width="16" height="16" viewBox="0 0 16 16"><path d="M1 7 L15 1 L10 15 L8 9 Z" fill="#fff"/></svg>Send Now</div>
</section>
<div class="abs map" role="img" aria-label="Map showing the company location"></div>

<!-- newsletter -->
<section class="abs news">
  <div class="n-k">Newsletter</div>
  <h2 class="n-h">Subscribe</h2>
  <div class="n-in"><svg width="14" height="11" viewBox="0 0 14 11"><rect x="0.5" y="0.5" width="13" height="10" fill="none" stroke="#9aa0a8"/><path d="M0.5 0.5 L7 6 L13.5 0.5" fill="none" stroke="#9aa0a8"/></svg>Enter Email Address</div>
  <div class="n-btn">Signup</div>
  <div class="follow">Follow Us</div>
  <div class="social" style="left:928px;background:#3b5fbf" aria-label="Social network link"></div>
  <div class="social" style="left:988px;background:#2ea6e8" aria-label="Social network link"></div>
  <div class="social" style="left:1047px;background:#e0433f" aria-label="Video channel link"></div>
</section>

<!-- footer -->
<footer class="abs footer">
  <div class="logo">ROLV</div>
  <p class="f-about">Clarovent services techniques grenoble. The solution to your maintenance problem</p>
  <div class="f-col" style="left:383px"><h4>SERVICES</h4><ul><li>Air conditioning</li><li>Heating</li><li>Air treatment</li></ul></div>
  <div class="f-col" style="left:635px"><h4>GET DIRECTION</h4>
    <div class="f-row"><svg width="10" height="14" viewBox="0 0 10 14"><path d="M5 0 C2 0 0 2 0 5 C0 8 5 14 5 14 C5 14 10 8 10 5 C10 2 8 0 5 0 Z" fill="var(--teal)"/><circle cx="5" cy="5" r="2" fill="#1f2830"/></svg><span>14 Rue des Tilleuls<br>38100 VALMONT LES PINS</span></div>
  </div>
  <div class="f-col" style="left:905px"><h4>Call Now for Services</h4>
    <div class="f-row"><svg width="13" height="13" viewBox="0 0 13 13"><path d="M2 0 L5 3 L3.5 5 C4.5 7 6 8.5 8 9.5 L10 8 L13 11 L11 13 C5 13 0 8 0 2 Z" fill="var(--teal)"/></svg><span>06 12 34 56 78<br>06 98 76 54 32</span></div>
    <h4 style="margin:28px 0 10px">Email Us</h4>
    <div class="f-row"><svg width="13" height="10" viewBox="0 0 13 10"><rect width="13" height="10" rx="1" fill="var(--teal)"/><path d="M0 0 L6.5 5 L13 0" stroke="#1f2830" fill="none"/></svg><span>contact@rolv-<br>services.fr</span></div>
  </div>
  <div class="line"></div>
  <div class="copy">&copy; 2020 <b>ROLV</b> All Right Reserved.</div>
  <div class="top-btn"><svg width="12" height="8" viewBox="0 0 12 8"><path d="M1 7 L6 2 L11 7" stroke="#fff" stroke-width="1.8" fill="none"/></svg></div>
</footer>

</body>
</html>
```